Wordpress website re-design

Update existing 5 page wordpress website to look more professional. We run a 10 week boxing program that ends in a black tie gala event.

We would like to keep the existing pink hero colour.

The website:
- must be Wordpress
- prefer it to work with the Elementor plugin for easy future changes
- Keep the existing URL structure
- Use white space/backgrounds - D not want all black background or the pink colour used as the background for an entire section
- Shouldn't look too 'templatey'. Good flow between sections

Logo, images and video to use can be found here: https://share.quorvexfiles.net/folders/8hTqzW2mLpRvBn4kXcYd_JsEaGfUoNiM-?view=public

Website to be redesigned: https://bellmoreshowcase.com.au/

Designs look the same

Target Market(s)

Men working office jobs aged 28-38

Coding

Coded - Design and coding required

Number of Pages Required

5+ page

Colors

Designer to choose colors to be used in the design.

Requirements
Must have
• Wordpress
Nice to have
• Work with Elementor so that I can easily make changes in the future
Should not have
• Entirely black background. Want it to be lighter / plenty of white background. Not too blocky - flowing through sections and some of the images with backgrounds removed to make it less blocky also. I do not want it to be clerly 'templatey'. The pink should be used as a hero colour, not for entire sections

```html
<!DOCTYPE html>
<html lang="en">
<head>
<meta charset="utf-8">
<title>Bout for Good — From Desk to the Ring in 10 Weeks</title>
<link href="https://fonts.googleapis.com/css2?family=Poppins:ital,wght@0,400;0,500;0,600;0,700;1,400&display=swap" rel="stylesheet">
<style>
:root{
  --pink:#e8096f;
  --ink:#2b2b2b;
  --muted:#555;
  --soft:#f7f7f7;
  --line:#e6e6e6;
  --white:#fff;
  --dark:#1c1c1c;
}
*{box-sizing:border-box;margin:0;padding:0}
html,body{width:1200px;height:5240px;overflow:hidden}
body{position:relative;font-family:'Poppins',sans-serif;color:var(--ink);background:var(--white)}
.abs{position:absolute}
.band{position:absolute;left:0;width:1200px}
.center{text-align:center}
.btn-pink{background:var(--pink);color:var(--white);display:flex;align-items:center;justify-content:center}
.btn-outline{border:1.5px solid var(--pink);color:var(--pink);font-size:16px;display:flex;align-items:center;justify-content:center;width:162px;height:42px;background:var(--white)}
.section-title{position:absolute;left:0;width:1200px;text-align:center;color:var(--pink);font-size:38px;font-weight:400;letter-spacing:.5px}
.section-sub{position:absolute;left:0;width:1200px;text-align:center;color:var(--muted);font-size:19px}
.wordmark{font-weight:600;color:var(--pink);letter-spacing:1px;line-height:1.05;text-transform:uppercase}
/* header */
.nav a{position:absolute;top:64px;font-size:15px;color:var(--ink);text-decoration:none}
.nav .active{color:var(--pink);border-bottom:2px solid var(--pink);padding-bottom:2px;font-size:17px;top:61px}
/* pillars */
.pillar{position:absolute;top:1131px;width:326px;height:431px;background:#f1f1f1;border-radius:12px;text-align:center}
.pillar h3{margin-top:16px;color:var(--pink);font-size:24px;font-weight:600}
.pillar p{margin-top:12px;font-size:17px;color:#333}
.pillar .photo{position:absolute;left:63px;top:124px;width:200px;height:200px;border-radius:50%;background:radial-gradient(circle at 50% 40%,#6b5a55,#262323)}
.pillar .explore{position:absolute;left:50px;top:353px;width:226px;height:44px;border-radius:22px;background:var(--white);font-size:19px;display:flex;align-items:center;justify-content:center}
/* features */
.feature{position:absolute;width:336px;text-align:center}
.feature .icon{width:96px;height:96px;border-radius:50%;border:3px solid var(--pink);margin:0 auto;display:flex;align-items:center;justify-content:center}
.feature .icon span{width:80px;height:80px;border-radius:50%;background:var(--pink);display:flex;align-items:center;justify-content:center}
.feature h4{margin-top:26px;font-size:19px;font-weight:400;line-height:28px;height:56px;text-transform:uppercase}
.feature p{margin-top:14px;font-size:14px;color:#444;line-height:23px;height:70px;padding:0 14px}
.feature .btn-outline{margin:16px auto 0}
/* blogs */
.blog{position:absolute;top:3648px;width:323px;height:340px;background:var(--white)}
.blog .photo{height:162px;position:relative}
.blog .date{position:absolute;left:18px;bottom:14px;color:var(--white);font-size:14px}
.blog p{margin:26px 20px 0;font-size:17px;line-height:21px;color:#333}
.blog .more{margin:18px 20px 0;color:var(--pink);font-size:19px;font-weight:500}
/* testimonials */
.review{position:absolute;top:4413px;width:500px;height:277px;background:var(--soft);text-align:center}
.review .stars{margin-top:30px;color:#f5a623;font-size:26px;letter-spacing:3px}
.review .name{margin-top:2px;color:var(--pink);font-size:21px}
.review .role{font-style:italic;font-size:17px;color:#333}
.review .quote{margin:14px 60px 0;font-size:17px;line-height:26px;color:#333}
.avatar{position:absolute;top:4303px;width:114px;height:114px;border-radius:50%}
/* footer */
.footer{background:var(--soft);border-top:4px solid var(--pink)}
.footer h5{position:absolute;top:106px;color:var(--ink);font-size:20px;font-weight:600}
.footer .rule{position:absolute;top:144px;width:38px;height:3px;background:var(--pink)}
.links{list-style:none}
.links li{color:var(--ink);font-size:15px;height:31px}
.links li::before{content:"›";margin-right:12px;font-size:18px;color:var(--pink)}
.social{position:absolute;top:261px;width:40px;height:40px;border-radius:50%;border:2px solid var(--pink)}
</style>
</head>
<body>

<!-- Header -->
<header class="band" style="top:0;height:150px;background:var(--white)">
  <div class="abs wordmark" style="left:84px;top:44px;font-size:28px;width:140px">Bout<br>for Good</div>
  <nav class="nav">
    <a class="active" style="left:507px">Home</a>
    <a style="left:586px">About Us</a>
    <a style="left:680px">Our Services</a>
    <a style="left:800px">blogs</a>
    <a style="left:868px">Testimonials</a>
  </nav>
  <div class="abs btn-pink" style="left:995px;top:58px;width:118px;height:36px;font-size:15px">Contact Us</div>
</header>

<!-- Hero -->
<section class="band" style="top:150px;height:743px;background:var(--soft)">
  <h1 class="abs" style="left:90px;top:136px;font-size:62px;line-height:74px;font-weight:400;color:#222">
    <span style="color:var(--pink);font-weight:700">FROM DESK TO</span><br>THE RING IN 10<br>WEEKS!
  </h1>
  <p class="abs" style="left:91px;top:384px;width:460px;font-size:17px;line-height:26px;color:#222">We help people like you go from little or no boxing experience to a boxing bout in 10 weeks. Get fit charity in a safe environment.</p>
  <div class="abs btn-pink" style="left:90px;top:510px;width:166px;height:46px;font-size:20px">Read More</div>
  <svg class="abs" style="left:310px;top:508px" width="48" height="48" viewBox="0 0 48 48"><circle cx="24" cy="24" r="23" fill="var(--pink)"/><path d="M19 14 L34 24 L19 34Z" fill="#fff"/></svg>
  <div class="abs" style="left:365px;top:515px;font-size:21px;color:#111">Watch Videos</div>
  <div class="abs" role="img" aria-label="Boxer in red kit walking to the ring at a black tie fight night" style="left:601px;top:82px;width:518px;height:585px;background:linear-gradient(160deg,#4a3b33,#1d1714 60%,#3a2a22)">
    <svg class="abs" style="left:235px;top:225px" width="50" height="50" viewBox="0 0 50 50"><circle cx="25" cy="25" r="24" fill="#fff"/><path d="M20 15 L35 25 L20 35Z" fill="#111"/></svg>
  </div>
</section>

<!-- What is -->
<section class="band" style="top:893px;height:834px;background:var(--white)">
  <h2 class="section-title" style="top:96px">WHAT IS BOUT FOR GOOD?</h2>
  <p class="section-sub" style="top:158px">10 Weeks, 30 Training Sessions, 1 Fight Night</p>
</section>
<div class="pillar" style="left:102px">
  <h3>HEALTH</h3><p>Lose Weight &amp; Get Fit</p>
  <div class="photo" role="img" aria-label="Guests celebrating at the black tie gala"></div>
  <div class="explore">Explore Now</div>
</div>
<div class="pillar" role="img" aria-label="Two boxers in headgear exchanging punches" style="left:436px;background:linear-gradient(170deg,#2d3140,#0f1118 55%,#3a1418);border:3px solid #ddd">
  <h3 style="color:#fff;margin-top:32px">COMMITMENT</h3>
  <div class="explore" style="background:var(--pink);color:#fff">Explore Now</div>
</div>
<div class="pillar" style="left:770px">
  <h3>KNOWLEGE</h3><p>Learn Valuable Boxing Skills</p>
  <div class="photo" role="img" aria-label="Guests celebrating at the black tie gala"></div>
  <div class="explore">Explore Now</div>
</div>

<!-- Why choose -->
<section class="band" style="top:1727px;height:1118px;background:var(--soft)">
  <h2 class="section-title" style="top:86px">WHY CHOOSE BOUT FOR GOOD?</h2>
  <p class="section-sub" style="top:146px;font-size:18px">The Faces Behind Our Success</p>
</section>
<div class="feature" style="left:95px;top:1968px">
  <div class="icon"><span><svg width="40" height="40" viewBox="0 0 40 40"><path d="M20 4 L34 9 V20 C34 29 27 34 20 36 C13 34 6 29 6 20 V9Z" fill="#fff"/><path d="M20 13 l2.5 5 5.5.6-4 3.8 1 5.4-5-2.7-5 2.7 1-5.4-4-3.8 5.5-.6z" fill="var(--pink)"/></svg></span></div>
  <h4>3 Weekly Training Sessions<br>for 10 Weeks</h4>
  <p>Training takes place each Tuesday, Thursday and Saturday throughout the 10 week program.</p>
  <div class="btn-outline">Read more</div>
</div>
<div class="feature" style="left:432px;top:1968px">
  <div class="icon"><span><svg width="40" height="40" viewBox="0 0 40 40"><circle cx="16" cy="22" r="10" fill="none" stroke="#fff" stroke-width="6" stroke-dasharray="4 3"/><circle cx="16" cy="22" r="4" fill="#fff"/><circle cx="29" cy="11" r="6" fill="none" stroke="#fff" stroke-width="4" stroke-dasharray="3 2"/></svg></span></div>
  <h4>Fight Kit</h4>
  <p>We provide a full fight kit so that you're ready to train from day 1. This includes boxing gloves, wraps and head gear.</p>
  <div class="btn-outline">Read more</div>
</div>
<div class="feature" style="left:769px;top:1968px">
  <div class="icon"><span><svg width="40" height="40" viewBox="0 0 40 40" fill="none" stroke="#fff" stroke-width="2.5"><ellipse cx="20" cy="20" rx="16" ry="6"/><ellipse cx="20" cy="20" rx="16" ry="6" transform="rotate(60 20 20)"/><ellipse cx="20" cy="20" rx="16" ry="6" transform="rotate(-60 20 20)"/><circle cx="20" cy="20" r="2.5" fill="#fff"/></svg></span></div>
  <h4>Membership to Steadfast<br>Boxing</h4>
  <p>All Bout for Good fighters receive full membership to Steadfast Boxing for the duration of the program.</p>
  <div class="btn-outline">Read more</div>
</div>
<div class="feature" style="left:95px;top:2394px">
  <div class="icon"><span><svg width="40" height="40" viewBox="0 0 40 40"><path d="M20 4 L34 9 V20 C34 29 27 34 20 36 C13 34 6 29 6 20 V9Z" fill="#fff"/><path d="M20 13 l2.5 5 5.5.6-4 3.8 1 5.4-5-2.7-5 2.7 1-5.4-4-3.8 5.5-.6z" fill="var(--pink)"/></svg></span></div>
  <h4>Black Tie Fight Event</h4>
  <p>Experience the glory of fighting in front of your friends, family and co-workers</p>
  <div class="btn-outline">Read more</div>
</div>
<div class="feature" style="left:432px;top:2394px">
  <div class="icon"><span><svg width="40" height="40" viewBox="0 0 40 40"><circle cx="16" cy="22" r="10" fill="none" stroke="#fff" stroke-width="6" stroke-dasharray="4 3"/><circle cx="16" cy="22" r="4" fill="#fff"/><circle cx="29" cy="11" r="6" fill="none" stroke="#fff" stroke-width="4" stroke-dasharray="3 2"/></svg></span></div>
  <h4>World Class Trainers</h4>
  <p>Be trained by the best of the best, including active professional boxers.</p>
  <div class="btn-outline">Read more</div>
</div>
<div class="feature" style="left:769px;top:2394px">
  <div class="icon"><span><svg width="40" height="40" viewBox="0 0 40 40" fill="none" stroke="#fff" stroke-width="2.5"><ellipse cx="20" cy="20" rx="16" ry="6"/><ellipse cx="20" cy="20" rx="16" ry="6" transform="rotate(60 20 20)"/><ellipse cx="20" cy="20" rx="16" ry="6" transform="rotate(-60 20 20)"/><circle cx="20" cy="20" r="2.5" fill="#fff"/></svg></span></div>
  <h4>Fair Matchmaking</h4>
  <p>Our experienced trainers will ensure you are matched with someone of a comparable skill level and size.</p>
  <div class="btn-outline">Read more</div>
</div>

<!-- Call to action -->
<section class="band" style="top:2845px;height:579px;background:var(--white)">
  <div class="abs" role="img" aria-label="Boxer training in a dim gym" style="left:88px;top:153px;width:1032px;height:272px;border-radius:20px;background:linear-gradient(100deg,#3c3f45,#1b1c1f 45%,#0d0d0e)">
    <h2 class="abs center" style="left:0;width:100%;top:56px;color:#fff;font-size:39px;font-weight:500">YOUR FIRST FIGHT STARTS HERE</h2>
    <p class="abs center" style="left:0;width:100%;top:126px;color:#fff;font-size:24px;font-weight:500">Register Your Interest In Less than 5 mins</p>
    <div class="abs btn-pink" style="left:404px;top:198px;width:224px;height:46px;border-radius:23px;font-size:20px">Explore Now</div>
  </div>
</section>

<!-- Blogs -->
<section class="band" style="top:3424px;height:676px;background:var(--soft)">
  <h2 class="section-title" style="top:84px">OUR LATEST BLOGS</h2>
</section>
<article class="blog" style="left:88px">
  <div class="photo" role="img" aria-label="Two boxers sparring in a smoky gym" style="background:linear-gradient(180deg,#3d5a5a,#1c2526)"><span class="date">September 24, 2023</span></div>
  <p>Risus commodo viverra made maecenas accumsan lacus vel facilisis.</p><div class="more">READ MORE</div>
</article>
<article class="blog" style="left:439px">
  <div class="photo" role="img" aria-label="Modern glass building against a blue sky" style="background:linear-gradient(160deg,#6fc3d8,#2a6f86 60%,#1b3a48)"><span class="date">September 24, 2023</span></div>
  <p>Risus commodo viverra made maecenas accumsan lacus vel facilisis.</p><div class="more">READ MORE</div>
</article>
<article class="blog" style="left:789px">
  <div class="photo" role="img" aria-label="Two businessmen shaking hands in an office" style="background:linear-gradient(180deg,#e6e9ee,#7c8796 70%,#2c3440)"><span class="date">September 24, 2023</span></div>
  <p>Risus commodo viverra made maecenas accumsan lacus vel facilisis.</p><div class="more">READ MORE</div>
</article>

<!-- Testimonials -->
<section class="band" style="top:4100px;height:630px;background:var(--white)">
  <h2 class="section-title" style="top:74px">CLIENT’S TESTIMONIALS</h2>
</section>
<div class="review" style="left:96px">
  <div class="stars">★★★★★</div><div class="name">Shane Wallis</div><div class="role">Organiser</div>
  <p class="quote">Lorem ipsum dolor sit amet, conse tetur adipiscing elit, sed do eiusmod tempor lacus vel facilisis.</p>
</div>
<div class="review" style="left:612px">
  <div class="stars">★★★★★</div><div class="name">Franklin Moss</div><div class="role">Organiser</div>
  <p class="quote">Lorem ipsum dolor sit amet, conse tetur adipiscing elit, sed do eiusmod temcumsan lacus vel facilisis.</p>
</div>
<div class="avatar" role="img" aria-label="Client portrait" style="left:288px;background:radial-gradient(circle,#f2b63a,#d98f18)"></div>
<div class="avatar" role="img" aria-label="Client portrait" style="left:804px;background:radial-gradient(circle,#8fb3bb,#5b8089)"></div>

<!-- Footer -->
<footer class="band footer" style="top:4730px;height:420px">
  <div class="abs wordmark" style="left:200px;top:136px;font-size:34px;width:200px">Bout<br>for Good</div>
  <div class="social" style="left:195px"></div>
  <div class="social" style="left:246px"></div>
  <div class="social" style="left:297px"></div>
  <div class="social" style="left:348px"></div>
  <h5 style="left:520px">Quick Links</h5><div class="rule" style="left:520px"></div>
  <ul class="abs links" style="left:525px;top:180px">
    <li>Home</li><li>About Us</li><li>Our Services</li><li>Our Blogs</li><li>Testimonials</li>
  </ul>
  <h5 style="left:779px">Our Newsletter</h5><div class="rule" style="left:779px"></div>
  <p class="abs" style="left:779px;top:180px;width:260px;color:var(--ink);font-size:15px;line-height:21px">Subscribe our newsletter to get the latest news.</p>
  <div class="abs" style="left:779px;top:246px;width:251px;height:38px;background:var(--white);border:1px solid var(--line)"></div>
  <div class="abs btn-pink" style="left:779px;top:300px;width:125px;height:35px;font-size:13px">SUBSCRIBE</div>
</footer>
<div class="band center" style="top:5150px;height:90px;background:var(--dark);color:#fff;font-size:17px;font-weight:500;line-height:90px">All Rights Reserved @ Copyrights 2023</div>

</body>
</html>
```